The Harlow Reserve Web Site design

I need a web design for my luxury range of Terry Toweling and Spa Accessories for luxury upmarket hotels and Spas. I have a catalog that sets the mood and tone I am looking for. I need a website design that shows off the look and feel of this luxury range while working back to the catalog look and feel. Its all about Upmarket and Luxury. I will be using the website as a reference site and as a site that customers can purchase off.
The Logo is attached as is the catalog. I don't mind changing the color of the Logo to match the website. However I would prefer to keep the font of that logo.

http://thegalleryloft.pixvaultex.com/p204519873
Please can you try and access this link. The Harlow Reserve
Name Bettina. Email bettina@kestrelsupplyco.com.au. Password Harlow.
These images are to be used for shopping page and please use the close up details of texture as background on pages and use those texture details and close ups for banners

Please note the look and feel has to be very upmarket and super luxury. Ficus is on mood and not on retail.
Have a look at the mood on the following websites
Www.gracefulretreatsex.com
And ourquietcovecottagestore.com
That one is retail .mi don't want retail focus but it's very clean. And simple and colors are good

Please rebook brief. I have added some important detail. Thanks

Relook brief. I have added,important detail. Thanks

Target Market(s)

Corporate buyers
This is not for retail selling to consumers
Price it's viewed only after secure login

Industry/Entity Type

Shopping

Colors
acd037
cadf82
fbc995
fce7d3
faa54b

Requirements
Must have
• Luxury. Think luxury. Very high end yet modern like the catalogue
Use banners on home page
Should not have
• Don't use the blue as the main color. It's too cheap.
No products on home page

```html
<!DOCTYPE html>
<html lang="en">
<head>
<meta charset="utf-8">
<title>The Harlow Reserve</title>
<link href="https://fonts.googleapis.com/css2?family=Raleway:wght@300;400;600;700&family=Open+Sans:wght@400;600;700&display=swap" rel="stylesheet">
<style>
:root{
  --green:#acd037;
  --green-dark:#8fb22a;
  --green-soft:#cadf82;
  --peach:#fbc995;
  --cream:#fce7d3;
  --orange:#faa54b;
  --orange-deep:#f28a2e;
  --teal:#2b8db3;
  --ink:#4a4a4a;
  --grey:#8a8a8a;
  --line:#e4e4e4;
  --night:#262626;
}
*{margin:0;padding:0;box-sizing:border-box}
html,body{width:705px;height:1200px;overflow:hidden;background:#fff}
body{font-family:"Open Sans",Arial,sans-serif;color:var(--ink);position:relative}
.abs{position:absolute}

/* header */
.brand{left:22px;top:14px}
.brand-name{font-family:"Raleway",Arial,sans-serif;font-weight:600;font-size:33px;color:var(--teal);letter-spacing:.2px;line-height:1}
.brand-tag{font-size:13px;color:var(--orange-deep);margin-top:6px}
.care{right:24px;top:20px;display:flex;align-items:center;gap:8px;font-size:13px;font-weight:600;color:var(--orange-deep)}
.care-icon{width:20px;height:20px;border-radius:4px;background:var(--green);display:flex;align-items:center;justify-content:center}

/* nav */
.nav{left:0;top:122px;width:705px;height:34px;background:var(--green);display:flex;align-items:center;padding:0 20px}
.nav a{color:#fff;font-size:11px;text-decoration:none;margin-right:22px;padding:4px 12px;border-radius:2px}
.nav a.active{background:var(--green-dark)}
.nav .cart{margin-left:auto;color:#fff;font-size:11px;font-weight:600;margin-right:10px}
.nav .search{width:150px;height:20px;background:#fff;border-radius:2px;display:flex;justify-content:flex-end}
.nav .search span{width:20px;height:20px;background:var(--orange);border-radius:0 2px 2px 0}

/* hero */
.hero{left:0;top:162px;width:705px;height:232px;background:linear-gradient(90deg,#f6f6f4,#ededeb)}
.hero-copy{left:70px;top:28px;text-align:center;width:300px}
.hero-kicker{font-size:10px;color:var(--grey);letter-spacing:.5px}
.hero-title{font-family:"Raleway",Arial,sans-serif;font-weight:300;font-size:33px;line-height:1.1;color:#7d8f6a;margin-top:6px;letter-spacing:.5px}
.hero-sub{font-family:"Raleway",Arial,sans-serif;font-weight:400;font-size:21px;color:var(--orange-deep);margin-top:6px;letter-spacing:.5px}
.btn{display:inline-block;background:var(--orange);color:#fff;font-size:10px;font-weight:600;padding:6px 16px;border-radius:2px}
.hero-copy .btn{margin-top:16px;background:#f57e5a}
.hero-photo{left:390px;top:40px;width:270px;height:180px;border-radius:6px;background:linear-gradient(180deg,#b04b45 0%,#a84a44 30%,#8f9a84 55%,#6f8a5c 100%)}
.arrow-edge{top:68px;width:12px;height:34px;background:#ddd;display:flex;align-items:center;justify-content:center}

/* newsletter strip */
.strip{left:0;top:412px;width:705px;height:40px;background:var(--cream);display:flex;align-items:center;padding:0 24px;font-size:10px}
.strip .field{width:110px;height:18px;background:#fff;margin-left:10px;border:1px solid var(--line);font-size:8px;color:#aaa;padding:3px 6px}
.strip .go{width:18px;height:18px;background:var(--orange)}
.strip .find{margin-left:auto;margin-right:12px}
.social-dot{width:26px;height:26px;border-radius:50%;background:#fff;border:1px solid var(--line);margin-left:8px}

/* promo grid */
.promo{top:476px;border-radius:3px;overflow:hidden}
.promo-a{left:70px;width:280px;height:210px;background:linear-gradient(90deg,#d9d4cc,#efeae4)}
.promo-a .label{position:absolute;right:14px;top:44px;text-align:center;font-family:"Raleway",Arial,sans-serif}
.promo-a .label b{display:block;font-weight:300;font-size:18px;color:#777}
.promo-a .label em{display:block;font-style:normal;font-size:30px;color:var(--orange);letter-spacing:1px;line-height:1.1}
.promo-b{left:352px;width:283px;height:104px;background:linear-gradient(90deg,#cfcac3,#efece8)}
.promo-b .label{position:absolute;left:16px;top:12px;font-family:"Raleway",Arial,sans-serif;color:var(--green-dark)}
.promo-b .label b{font-weight:400;font-size:12px;display:block}
.promo-b .label em{font-style:normal;font-size:26px;font-weight:300;display:block;line-height:1}
.promo-b .label small{font-size:7px;color:var(--grey)}
.promo-c{left:352px;top:582px;width:155px;height:104px;background:linear-gradient(160deg,#b8ad9e,#8c7f70)}
.promo-c .label{position:absolute;left:10px;bottom:22px;color:#fff;font-family:"Raleway",Arial,sans-serif;font-size:14px;font-weight:600;line-height:1.05}
.promo-d{left:509px;top:582px;width:126px;height:104px;background:linear-gradient(160deg,#e9e7e3,#cfcbc5)}
.promo-d .label{position:absolute;left:12px;top:10px;color:#fff;font-family:"Raleway",Arial,sans-serif;font-size:22px;font-weight:700;line-height:1}
.promo-d .label small{display:block;font-size:8px;font-weight:400}
.promo .btn{position:absolute;font-size:7px;padding:3px 8px}

/* tabs + products */
.tabs{left:70px;top:702px;width:565px;height:24px;background:#fff;display:flex;font-size:9px;font-weight:600;border-bottom:1px solid var(--line)}
.tabs span{padding:6px 14px;color:var(--grey)}
.tabs span.on{background:var(--orange);color:#fff;border-radius:3px 3px 0 0}
.tabs .pager{margin-left:auto;width:20px;height:20px;background:#e5e5e5;margin-top:2px}
.shelf{left:0;top:726px;width:705px;height:200px;background:var(--peach)}
.card{top:14px;width:112px;height:172px;background:#fff;border:1px solid #f0d9c0}
.card.lift{top:4px;box-shadow:0 4px 10px rgba(0,0,0,.22)}
.card .pic{margin:8px;height:92px;background:linear-gradient(160deg,#fafafa,#dcdcdc)}
.card .model{font-size:6px;color:var(--grey);text-align:center}
.card .name{font-size:9px;font-weight:600;text-align:center;margin-top:3px;color:#555}
.card .btn{display:block;width:60px;margin:6px auto 0;font-size:6px;padding:3px 0;text-align:center}
.card .flag{position:absolute;left:0;top:0;width:0;height:0;border-top:16px solid var(--orange);border-right:16px solid transparent}

/* about */
.about{left:70px;top:946px;width:565px;text-align:center}
.about h2{font-family:"Raleway",Arial,sans-serif;font-weight:600;font-size:17px;color:#555}
.about p{font-size:7.5px;line-height:1.55;color:var(--grey);text-align:left;margin-top:10px}

/* footer */
.foot{left:70px;top:1056px;width:565px;display:flex;gap:30px;font-size:7.5px;color:var(--grey)}
.foot h4{font-size:9px;color:#444;margin-bottom:5px}
.foot li{list-style:none;line-height:1.5}
.socials{display:grid;grid-template-columns:repeat(3,18px);gap:5px}
.socials i{width:18px;height:18px;border-radius:50%;background:#555;display:block}
.seal{left:594px;top:1066px;width:42px;height:42px;border-radius:50%;border:3px double #bbb}
.bottom{left:0;top:1160px;width:705px;height:40px;background:var(--night);color:#bbb;font-size:7px;display:flex;align-items:center;padding:0 70px}
.bottom span{margin-right:12px}
.bottom .copy{margin-left:auto;text-align:right;margin-right:0}
</style>
</head>
<body>

<header>
  <div class="abs brand">
    <div class="brand-name">The Harlow Reserve</div>
    <div class="brand-tag">Luxury range of Terry Toweling and Spa Accessories</div>
  </div>
  <div class="abs care">
    <span class="care-icon"><svg width="12" height="12" viewBox="0 0 24 24"><path fill="#fff" d="M6.6 10.8a15 15 0 0 0 6.6 6.6l2.2-2.2c.3-.3.7-.4 1-.2 1.1.4 2.3.6 3.6.6.6 0 1 .4 1 1V20c0 .6-.4 1-1 1A17 17 0 0 1 3 4c0-.6.4-1 1-1h3.5c.6 0 1 .4 1 1 0 1.3.2 2.5.6 3.6.1.3 0 .7-.2 1z"/></svg></span>
    CUSTOM CARE: 888-55-0192
  </div>
</header>

<nav class="abs nav">
  <a class="active">Home</a><a>About</a><a>Products</a><a>Services</a><a>Contact</a>
  <span class="cart">My cart</span>
  <div class="search"><span></span></div>
</nav>

<section class="abs hero">
  <div class="abs arrow-edge" style="left:0"><svg width="6" height="10"><path d="M5 1 1 5l4 4" stroke="#888" fill="none"/></svg></div>
  <div class="abs arrow-edge" style="right:0"><svg width="6" height="10"><path d="m1 1 4 4-4 4" stroke="#888" fill="none"/></svg></div>
  <div class="abs hero-copy">
    <div class="hero-kicker">Luxury Range</div>
    <div class="hero-title">TERRY TOWELING<br>&amp; SPA ACCESSORIES</div>
    <div class="hero-sub">THE HARLOW RESERVE</div>
    <span class="btn">SHOP NOW</span>
  </div>
  <div class="abs hero-photo" role="img" aria-label="Stack of folded terry towels in red, rose and green"></div>
</section>

<section class="abs strip">
  <span>Stay updated</span>
  <span class="field">Your email address</span><span class="go"></span>
  <span class="find">Find us on</span>
  <span class="social-dot"></span><span class="social-dot"></span><span class="social-dot"></span>
</section>

<section>
  <div class="abs promo promo-a" role="img" aria-label="Woman in a white bathrobe beside a bath mat">
    <div class="label"><b>BEST</b><em>CANELADO<br>&amp;<br>BATH MAT</em></div>
  </div>
  <div class="abs promo promo-b" role="img" aria-label="Guest relaxing on a spa bed wrapped in a towel">
    <div class="label"><b>Body</b><em>WRAP</em><small>COLLECTION</small></div>
  </div>
  <div class="abs promo promo-c" role="img" aria-label="Massage table cover in a spa room">
    <div class="label">FUNDA CAMILLA<br>DE MASAJES</div>
    <span class="btn" style="left:10px;bottom:6px">SHOP NOW</span>
  </div>
  <div class="abs promo promo-d" role="img" aria-label="Folded white top sheet">
    <div class="label">TOP<br>SHEET<small>COLLECTION</small></div>
    <span class="btn" style="right:8px;bottom:6px">SHOP NOW</span>
  </div>
</section>

<div class="abs tabs"><span class="on">NEW PRODUCTS</span><span>FEATURED</span><span>LATEST</span><span class="pager"></span></div>

<section class="abs shelf">
  <div class="abs card" style="left:-88px"><div class="pic" role="img" aria-label="Folded white towel"></div><div class="model">MODEL 897-3</div><div class="name">BODY WRAP / PAREO</div><span class="btn">ADD TO CART</span></div>
  <div class="abs card" style="left:35px"><div class="flag"></div><div class="pic" role="img" aria-label="Folded white towel"></div><div class="model">MODEL 897-3</div><div class="name">BODY WRAP / PAREO</div><span class="btn">ADD TO CART</span></div>
  <div class="abs card" style="left:159px"><div class="flag"></div><div class="pic" role="img" aria-label="Close up of white waffle towel"></div><div class="model">MODEL 897-3</div><div class="name">BODY WRAP / PAREO</div><span class="btn">ADD TO CART</span></div>
  <div class="abs card lift" style="left:283px"><div class="flag"></div><div class="pic" role="img" aria-label="Stacked white towels"></div><div class="model">MODEL 897-3</div><div class="name">BODY WRAP / PAREO</div><span class="btn">ADD TO CART</span></div>
  <div class="abs card" style="left:407px"><div class="flag"></div><div class="pic" role="img" aria-label="Rolled white towels"></div><div class="model">MODEL 897-3</div><div class="name">BODY WRAP / PAREO</div><span class="btn">ADD TO CART</span></div>
  <div class="abs card" style="left:531px"><div class="flag"></div><div class="pic" role="img" aria-label="Draped white body wrap"></div><div class="model">MODEL 897-3</div><div class="name">BODY WRAP / PAREO</div><span class="btn">ADD TO CART</span></div>
  <div class="abs card" style="left:655px"><div class="pic" role="img" aria-label="Folded white towel"></div><div class="model">MODEL 897-3</div><div class="name">BODY WRAP / PAREO</div><span class="btn">ADD TO CART</span></div>
</section>

<section class="abs about">
  <h2>About The Harlow Reserve</h2>
  <p>Lorem ipsum dolor sit amet, consectetur adipiscing elit. Quisque ac lorem sed velit posuere dapibus. Nullam convallis, lacus sed egestas tincidunt, arcu dui tempus justo, vel ultricies nibh metus in tellus. Duis sed odio sit amet nibh vulputate cursus a sit amet mauris. Morbi accumsan ipsum velit. Nam nec tellus a odio tincidunt auctor a ornare odio. Sed non mauris vitae erat consequat auctor eu in elit.</p>
  <p style="margin-top:6px">Class aptent taciti sociosqu ad litora torquent per conubia nostra, per inceptos himenaeos. Mauris in erat justo. Nullam ac urna eu felis dapibus condimentum sit amet a augue.</p>
</section>

<footer>
  <div class="abs foot">
    <div><h4>Customer Service</h4><ul><li>Contact</li><li>FAQ</li><li>Terms of payment</li><li>Terms of sale</li><li>Delivery terms and locations</li><li>Returns and Refunds</li></ul></div>
    <div><h4>Information</h4><ul><li>Lorem ipsum</li><li>Lorem ipsum</li><li>Lorem ipsum</li><li>Lorem ipsum</li><li>Lorem ipsum</li></ul></div>
    <div><h4>Campaigns</h4><ul><li>Lorem ipsum</li><li>Lorem ipsum</li><li>Lorem ipsum</li><li>Lorem ipsum</li><li>Lorem ipsum</li></ul></div>
    <div><h4>Stores</h4><ul><li>Paris</li><li>New York</li><li>London</li><li>Madrid</li><li>Tokyo</li></ul></div>
    <div><h4>Social</h4><div class="socials"><i></i><i></i><i></i><i></i><i></i><i></i></div></div>
  </div>
  <div class="abs seal"></div>
  <div class="abs bottom">
    <span>Privacy &amp; Cookies</span><span>Terms &amp; Conditions</span><span>Accessibility</span><span>Store Directory</span><span>About us</span>
    <span class="copy">© 2014 The Harlow Reserve<br>All Rights Reserved</span>
  </div>
</footer>

</body>
</html>
```